Van wrap design

Hello I have a customer wanting a van wrapped.. Already has logo and everything just wants a design for the van to make it pop!
The files uploaded are the old van design please jazz it up make it pop change it how ever to look better!!!
This needs to be a full wrap design!
Colors: Blue, Maroon, Yellow, Gray, White

Name is: Brask in big letters LLC small next to brask
and plumbing below Brask

Company name Brask Plumbing LLC
I have file for logo guy!

Please let me know!
Also if you look at attached images the logo guy with the blue background we like that background try something with that coming up from bottom of van!

Thank You

Thank You
Tobin
Updates

Project Deadline Extended
Reason: Need better designs!!!

Time Extended and payment gauranteed!!!!!!!

Industry/Entity Type

It Company

Requirements
Must have
• Logo guy is big priority, wants alot of attention from this wrap!

```html
<!DOCTYPE html>
<html lang="en">
<head>
<meta charset="utf-8">
<title>Brask Plumbing LLC – Van Rear Wrap</title>
<link href="https://fonts.googleapis.com/css2?family=Roboto:wght@700&family=Roboto+Condensed:wght@700&family=Kaushan+Script&display=swap" rel="stylesheet">
<style>
  :root {
    --page: #ffffff;
    --van-black: #1c1c1c;
    --wrap-blue-top: #2f63d6;
    --wrap-blue-bottom: #22309c;
    --band-navy: #2a2a8a;
    --stripe-yellow: #f5c400;
    --light-red: #e8601a;
    --light-amber: #f6b21a;
    --tire-gray: #c4c4c6;
    --axle-gray: #a9a9ab;
    --text-white: #ffffff;
    --plate-black: #161616;
  }
  html, body {
    margin: 0;
    width: 1200px;
    height: 900px;
    overflow: hidden;
    background: var(--page);
  }
  .van-rear { display: block; width: 1200px; height: 900px; }
  .tagline { font-family: "Roboto", Arial, sans-serif; font-weight: 700; fill: var(--text-white); }
  .company-name { font-family: "Roboto Condensed", Arial, sans-serif; font-weight: 700; fill: var(--text-white); }
  .contact-line { font-family: "Roboto Condensed", Arial, sans-serif; font-weight: 700; fill: var(--text-white); }
  .slogan { font-family: "Kaushan Script", cursive; fill: var(--text-white); }
</style>
</head>
<body>
<svg class="van-rear" viewBox="0 0 1200 900" xmlns="http://www.w3.org/2000/svg">
  <defs>
    <linearGradient id="wrap-blue" x1="0" y1="0" x2="0" y2="1">
      <stop offset="0" stop-color="var(--wrap-blue-top)"/>
      <stop offset="1" stop-color="var(--wrap-blue-bottom)"/>
    </linearGradient>
    <linearGradient id="tail-light" x1="0" y1="0" x2="1" y2="0">
      <stop offset="0" stop-color="var(--light-red)"/>
      <stop offset="0.5" stop-color="var(--light-amber)"/>
      <stop offset="1" stop-color="var(--light-red)"/>
    </linearGradient>
    <linearGradient id="mascot-tones" x1="0" y1="0" x2="0" y2="1">
      <stop offset="0" stop-color="#f2a65a"/>
      <stop offset="0.5" stop-color="#6fa8e8"/>
      <stop offset="1" stop-color="#b8242c"/>
    </linearGradient>
  </defs>

  <!-- wheels and axle -->
  <g class="running-gear">
    <rect x="255" y="700" width="85" height="180" rx="16" fill="var(--tire-gray)"/>
    <rect x="855" y="700" width="88" height="180" rx="16" fill="var(--tire-gray)"/>
    <rect x="240" y="672" width="715" height="42" rx="12" fill="var(--axle-gray)"/>
  </g>

  <!-- body -->
  <path class="van-body" d="M292 76 Q244 80 238 200 L232 645 L968 645 L962 200 Q956 80 908 76 Z" fill="var(--van-black)"/>
  <rect class="roof-light" x="560" y="76" width="80" height="19" fill="url(#tail-light)"/>

  <path class="wrap-panel" d="M305 95 Q276 100 270 210 L268 632 L932 632 L930 210 Q924 100 895 95 Z" fill="url(#wrap-blue)"/>

  <rect class="tail-light" x="248" y="210" width="38" height="132" fill="url(#tail-light)"/>
  <rect class="tail-light" x="908" y="210" width="38" height="132" fill="url(#tail-light)"/>

  <!-- heading -->
  <text class="tagline" x="600" y="145" font-size="27" text-anchor="middle">Your Plumping Contractor</text>

  <!-- company name -->
  <text class="company-name" x="345" y="272" font-size="128" textLength="340" lengthAdjust="spacingAndGlyphs">BRASK</text>
  <text class="company-name" x="697" y="272" font-size="18">LLC</text>
  <text class="company-name" x="345" y="330" font-size="44" textLength="378" lengthAdjust="spacing">PLUMBING</text>

  <!-- mascot area -->
  <rect class="mascot" role="img" aria-label="Company mascot: cartoon plumber with wrench and boxing gloves" x="745" y="145" width="140" height="205" rx="22" fill="url(#mascot-tones)"/>

  <!-- contacts -->
  <text class="contact-line" x="280" y="398" font-size="26">West: 317-555-0142</text>
  <text class="contact-line" x="280" y="437" font-size="26">South: 317-555-0187</text>
  <text class="contact-line" x="280" y="478" font-size="23">E-mail: tomr@braskllc.com</text>
  <text class="contact-line" x="570" y="405" font-size="40" textLength="300" lengthAdjust="spacingAndGlyphs">Toll Free: 800-555</text>

  <!-- plate recess and reflectors -->
  <rect class="plate-recess" x="628" y="425" width="182" height="87" rx="12" fill="var(--plate-black)"/>
  <rect class="reflector" x="302" y="532" width="131" height="16" fill="var(--text-white)"/>
  <rect class="reflector" x="770" y="532" width="135" height="16" fill="var(--text-white)"/>

  <!-- slogan band -->
  <g class="slogan-band">
    <rect x="268" y="558" width="664" height="4" fill="var(--stripe-yellow)"/>
    <rect x="268" y="565" width="664" height="56" fill="var(--band-navy)"/>
    <rect x="268" y="622" width="664" height="4" fill="var(--stripe-yellow)"/>
    <text class="slogan" x="597" y="603" font-size="32" text-anchor="middle">Take the Brask to your Pipes!</text>
  </g>

  <!-- bumper -->
  <rect class="bumper" x="235" y="633" width="730" height="60" rx="22" fill="var(--van-black)"/>
</svg>
</body>
</html>
```